TBranwell executive consulting

We need a basic clean website for executive consulting. Rosalind is the previos CIO for bluecrest airways and currently supports several technology companies with innovation and transformation.

Target Market(s)

C level technology and CIO training

Industry/Entity Type

Technology and travel industry

Coding

Coded - Design and coding required

Number of Pages Required

3 page

Font styles to use
Sans Serif

Colors
0054AA
0677BA
7BADD7
CADEEF
E8F1F8
0094D4
00A9DD
6FCCEA
C7EBF8
E9F6FB

Requirements
Must have
• Home page, about us, services social media links

```html
<!DOCTYPE html>
<html lang="en">
<head>
<meta charset="utf-8">
<title>TBranwell Executive Consulting</title>
<link rel="stylesheet" href="https://fonts.googleapis.com/css2?family=Bodoni+Moda:wght@400;500&family=Montserrat:wght@400;500;600;700&display=swap">
<style>
:root{
  --navy:#0054AA;
  --blue:#0677BA;
  --sky:#7BADD7;
  --mist:#CADEEF;
  --ice:#E8F1F8;
  --cyan:#0094D4;
  --aqua:#00A9DD;
  --aqua-light:#6FCCEA;
  --pale:#C7EBF8;
  --wash:#E9F6FB;
  --ink:#222428;
  --text:#3a3d42;
  --white:#ffffff;
  --grad:linear-gradient(90deg,#00A9DD 0%,#0677BA 100%);
}
*{box-sizing:border-box;margin:0;padding:0}
html,body{width:1200px;height:3940px;overflow:hidden}
body{font-family:'Montserrat',sans-serif;color:var(--text);background:var(--white);position:relative}
.serif{font-family:'Bodoni Moda',serif;font-weight:400}
.accent{color:var(--blue)}
.btn{display:inline-block;background:var(--grad);color:var(--white);font-size:13px;font-weight:600;letter-spacing:2px;text-transform:uppercase;border-radius:24px;padding:16px 28px;text-decoration:none}
.social{display:flex;gap:10px}
.social span{display:block;width:38px;height:38px;border:1.5px solid var(--blue);border-radius:50%;position:relative}
.social span::after{content:"";position:absolute;inset:12px;border-radius:3px;background:var(--blue)}
.brand{font-family:'Montserrat',sans-serif;font-weight:600;color:var(--navy);font-size:32px;letter-spacing:.5px;white-space:nowrap}

/* header */
.site-header{position:absolute;top:0;left:0;width:1200px;height:80px;background:var(--white)}
.site-header .brand{position:absolute;left:140px;top:20px}
.main-nav{position:absolute;left:371px;top:30px;display:flex;gap:33px;font-size:13px;font-weight:500;color:var(--ink)}
.site-header .social{position:absolute;left:648px;top:19px}
.call-bar{position:absolute;right:0;top:0;width:392px;height:80px;background:var(--grad);clip-path:polygon(22px 0,100% 0,100% 100%,0 100%)}
.call-bar .ring{position:absolute;left:4px;top:16px;width:48px;height:48px;border-radius:50%;background:var(--white);display:flex;align-items:center;justify-content:center}
.call-bar .lbl{position:absolute;left:60px;top:14px;color:var(--white);font-size:15px;font-weight:500}
.call-bar .num{position:absolute;left:60px;top:34px;color:var(--white);font-size:23px;font-weight:600;letter-spacing:2px}

/* hero */
.hero{position:absolute;top:80px;left:0;width:1200px;height:537px;background:linear-gradient(180deg,#3a3550 0%,#2b3a5c 45%,#1b3f63 70%,#0e2c4a 100%)}
.hero .scene{position:absolute;inset:0}
.hero .kicker{position:absolute;left:143px;top:138px;color:var(--white);font-size:23px;font-weight:500;letter-spacing:1px}
.hero h1{position:absolute;left:141px;top:172px;color:var(--white);font-size:56px;line-height:68px;font-weight:400;white-space:nowrap}
.hero .btn{position:absolute;left:142px;top:342px;padding:15px 27px}
.hero .arc{position:absolute;left:680px;top:140px;width:280px;height:300px;border:14px solid var(--cyan);border-radius:50%;border-bottom-color:transparent;border-right-color:transparent;transform:rotate(20deg)}
.hero .portrait{position:absolute;left:665px;top:50px;width:325px;height:487px;border-radius:150px 150px 0 0;background:linear-gradient(180deg,#6b4a3e 0%,#2a2c36 40%,#14161d 100%)}

/* about */
.about{position:absolute;top:617px;left:0;width:1200px;height:643px}
.about .frame{position:absolute;left:277px;top:71px;width:252px;height:337px;background:#3b3b3d}
.about .photo{position:absolute;left:107px;top:82px;width:411px;height:424px;background:linear-gradient(160deg,#1b3b8a 0%,#c8d4e6 35%,#c0394a 70%,#8d1d2a 100%);z-index:1}
.about .callbox{position:absolute;left:70px;top:421px;width:382px;height:203px;background:var(--grad);z-index:0}
.about .callbox .ring{position:absolute;left:36px;top:120px;width:46px;height:46px;border-radius:50%;background:var(--white);display:flex;align-items:center;justify-content:center}
.about .callbox .lbl{position:absolute;left:94px;top:122px;color:var(--white);font-size:13px;font-weight:500}
.about .callbox .num{position:absolute;left:94px;top:140px;color:var(--white);font-size:22px;font-weight:600;letter-spacing:2px}
.about .callbox .line{position:absolute;left:316px;top:156px;width:66px;height:1px;background:var(--pale)}
.about .copy{position:absolute;left:644px;top:122px;width:415px}
.about h2{font-size:36px;line-height:42px;color:var(--ink);margin-bottom:18px}
.about p{font-size:12.5px;line-height:21.6px;letter-spacing:.3px;margin-bottom:14px;color:var(--text)}
.about .btn{margin-top:14px;padding:15px 28px}

/* services */
.services{position:absolute;top:1260px;left:0;width:1200px;height:835px;background:var(--wash)}
.section-title{text-align:center;font-size:38px;color:var(--ink)}
.services .section-title{position:absolute;top:76px;width:100%}
.card{position:absolute;top:152px;width:290px;height:507px;background:var(--white);border-radius:10px;overflow:hidden}
.card .img{height:157px}
.card h3{color:var(--blue);font-size:21px;font-weight:600;line-height:28px;margin:24px 4px 14px 19px;white-space:nowrap}
.card ul{list-style:none;margin:0 16px 0 20px}
.card li{font-size:12px;line-height:21.6px;color:var(--text);padding-left:13px;position:relative;margin-bottom:12px}
.card li::before{content:"";position:absolute;left:0;top:8px;width:5px;height:5px;border-radius:50%;background:var(--blue)}
.card .btn{position:absolute;left:20px;bottom:33px;padding:15px 28px}
.slider-track{position:absolute;left:141px;top:723px;width:789px;height:2px;background:var(--mist)}
.slider-track i{position:absolute;left:162px;top:0;width:353px;height:2px;background:var(--cyan)}
.arrow{position:absolute;top:704px;width:40px;height:40px;border:1.5px solid var(--blue);border-radius:50%;display:flex;align-items:center;justify-content:center}

/* testimonials */
.testimonials{position:absolute;top:2095px;left:0;width:1200px;height:665px}
.testimonials .section-title{position:absolute;top:84px;width:100%}
.avatar{position:absolute;border-radius:50%;background:linear-gradient(180deg,#d7d9dc,#8a8f96)}
.testimonials .name{position:absolute;top:289px;width:100%;text-align:center;color:var(--blue);font-weight:600;font-size:18px}
.testimonials .quote{position:absolute;top:331px;left:246px;width:708px;text-align:center;font-size:13px;line-height:21.6px;color:var(--text)}
.testimonials .quote p{margin-bottom:13px}
.dots{position:absolute;top:566px;left:576px;display:flex;gap:10px}
.dots span{width:9px;height:9px;border-radius:50%;border:1px solid var(--blue)}
.dots span.on{background:var(--blue)}

/* cta */
.cta{position:absolute;top:2760px;left:0;width:1200px;height:412px;background:linear-gradient(90deg,#1a6fb3 0%,#1f80c6 50%,#3a93cf 100%)}
.cta h2{position:absolute;top:116px;width:100%;text-align:center;color:var(--white);font-size:40px;line-height:51px}
.cta .btn{position:absolute;left:523px;top:245px;background:var(--white);color:var(--blue);padding:15px 27px}

/* contact */
.contact{position:absolute;top:3172px;left:0;width:1200px;height:558px}
.contact .eyebrow{position:absolute;left:143px;top:127px;font-size:12px;font-weight:600;color:var(--ink)}
.contact h2{position:absolute;left:142px;top:148px;font-size:36px;color:var(--ink)}
.info{position:absolute;left:143px;display:flex;gap:21px}
.info .ico{width:52px;height:52px;border:1.5px solid var(--mist);border-radius:50%;display:flex;align-items:center;justify-content:center;flex:none}
.info b{display:block;font-size:16px;color:var(--ink);font-weight:700;margin-top:2px}
.info span{font-size:15px;line-height:20px;color:var(--ink)}
.form{position:absolute;left:568px;top:93px;width:491px;height:371px;border-radius:14px;background:linear-gradient(180deg,#4b4b4d 0%,#1b1b1c 100%)}
.field{position:absolute;border-bottom:1px solid #8e8e90;height:40px}
.field b{display:block;color:var(--white);font-size:11px;font-weight:600}
.field span{display:block;color:#b9b9bb;font-size:11px;margin-top:3px}
.form .btn{position:absolute;left:40px;top:278px;padding:15px 23px}
.dotgrid{position:absolute;left:918px;top:322px}

/* footer */
.site-footer{position:absolute;top:3730px;left:0;width:1200px;height:210px;background:linear-gradient(180deg,#00A9DD 0%,#0677BA 100%)}
.site-footer .brand{position:absolute;left:238px;top:78px;color:var(--white);font-size:32px}
.site-footer .divider{position:absolute;left:433px;top:60px;width:1px;height:120px;background:rgba(255,255,255,.35)}
.foot-nav{position:absolute;left:477px;top:62px;display:flex;gap:50px;color:var(--white);font-size:13px;font-weight:600}
.site-footer .copyright{position:absolute;left:477px;top:124px;color:var(--white);font-size:12.5px}
.site-footer .social{position:absolute;left:837px;top:117px;gap:8px}
.site-footer .social span{width:28px;height:28px;border-color:var(--white)}
.site-footer .social span::after{inset:9px;background:var(--white)}
</style>
</head>
<body>

<header class="site-header">
  <div class="brand">TBranwell</div>
  <nav class="main-nav"><span>HOME</span><span>ABOUT ME</span><span>SERVICES</span></nav>
  <div class="social"><span aria-label="Social link"></span><span aria-label="Social link"></span><span aria-label="Social link"></span></div>
  <div class="call-bar">
    <div class="ring"><svg width="22" height="22" viewBox="0 0 24 24"><path d="M6.6 10.8a15 15 0 0 0 6.6 6.6l2.2-2.2a1 1 0 0 1 1-.25 11.4 11.4 0 0 0 3.6.57 1 1 0 0 1 1 1V20a1 1 0 0 1-1 1A17 17 0 0 1 3 4a1 1 0 0 1 1-1h3.5a1 1 0 0 1 1 1c0 1.25.2 2.45.57 3.57a1 1 0 0 1-.25 1z" fill="#0677BA"/></svg></div>
    <div class="lbl">CALL ME TODAY</div>
    <div class="num">(123) 456-7890</div>
  </div>
</header>

<section class="hero">
  <div class="scene" role="img" aria-label="City skyline and suspension bridge at dusk"></div>
  <div class="arc"></div>
  <div class="portrait" role="img" aria-label="Portrait of Rosalind Branwell in a dark blazer"></div>
  <div class="kicker">CONSULTING FOR A</div>
  <h1 class="serif">Tech-Forward<br>Travel Experience</h1>
  <a class="btn">Contact Me</a>
</section>

<section class="about">
  <div class="frame"></div>
  <div class="callbox">
    <div class="ring"><svg width="20" height="20" viewBox="0 0 24 24"><path d="M6.6 10.8a15 15 0 0 0 6.6 6.6l2.2-2.2a1 1 0 0 1 1-.25 11.4 11.4 0 0 0 3.6.57 1 1 0 0 1 1 1V20a1 1 0 0 1-1 1A17 17 0 0 1 3 4a1 1 0 0 1 1-1h3.5a1 1 0 0 1 1 1c0 1.25.2 2.45.57 3.57a1 1 0 0 1-.25 1z" fill="#0677BA"/></svg></div>
    <div class="lbl">CALL ME TODAY</div>
    <div class="num">(123) 456-7890</div>
    <div class="line"></div>
  </div>
  <div class="photo" role="img" aria-label="Rosalind Branwell in a red jacket in front of an aircraft"></div>
  <div class="copy">
    <h2 class="serif">ABOUT<br>ROSALIND <span class="accent">BRANWELL</span></h2>
    <p>Rosalind A. Branwell is a retired Chief Executive Officer and Executive Advisor of Bluecrest Airways, a role she held from 2017 until December 2024. In this capacity, Ms. Branwell oversaw key strategic initiatives, including advising senior leadership on the company's technology roadmap and five-year strategic plan, optimizing workflow processes for the Technology Supply Chain, and mentoring the incoming Chief Information Officer.</p>
    <p>Prior to this role, Ms. Branwell served as Vice President of Business Transformation, Corporate Delivery, and Technology at Bluecrest Airways from 2012 to 2017, and as Vice President of Strategic Planning and Implementation from 2008 to 2012.</p>
    <a class="btn">Read More</a>
  </div>
</section>

<section class="services">
  <h2 class="section-title serif">SERVICES <span class="accent">OFFERED</span></h2>
  <article class="card" style="left:141px">
    <div class="img" role="img" aria-label="Audience attending a leadership session" style="background:linear-gradient(180deg,#cfc7bd,#6e655c)"></div>
    <h3>Leadership<br>Mentorship</h3>
    <ul>
      <li>Personalized coaching for IT leaders to develop strategic decision-making, emotional intelligence, and resilience.</li>
      <li>Mentorship programs for aspiring technology leaders to prepare for executive roles.</li>
    </ul>
    <a class="btn">Read More</a>
  </article>
  <article class="card" style="left:455px">
    <div class="img" role="img" aria-label="Professional reviewing notes in a notebook" style="background:linear-gradient(180deg,#e6e4e1,#b9ada0)"></div>
    <h3>Program &amp;<br>Project Oversight</h3>
    <ul>
      <li>Independent oversight of complex IT programs to ensure alignment with objectives and timelines.</li>
      <li>Risk assessment and mitigation for major technology initiatives.</li>
    </ul>
    <a class="btn">Read More</a>
  </article>
  <article class="card" style="left:769px">
    <div class="img" role="img" aria-label="Hands with digital data graphics over a desk" style="background:linear-gradient(180deg,#2e3f63,#a77458)"></div>
    <h3>Digital Transformation<br>Consulting</h3>
    <ul>
      <li>Assessing current digital maturity and identifying opportunities for improvement.</li>
      <li>Designing and implementing digital transformation initiatives, including agile methodologies and DevOps practices.</li>
    </ul>
    <a class="btn">Read More</a>
  </article>
  <div class="slider-track"><i></i></div>
  <div class="arrow" style="left:967px"><svg width="12" height="12" viewBox="0 0 12 12"><path d="M7.5 2 3.5 6l4 4" fill="none" stroke="#0677BA" stroke-width="1.5"/></svg></div>
  <div class="arrow" style="left:1019px"><svg width="12" height="12" viewBox="0 0 12 12"><path d="M4.5 2l4 4-4 4" fill="none" stroke="#0677BA" stroke-width="1.5"/></svg></div>
</section>

<section class="testimonials">
  <h2 class="section-title serif">CLIENT <span class="accent">TESTIMONIALS</span></h2>
  <div class="avatar" style="left:405px;top:172px;width:80px;height:80px" role="img" aria-label="Client portrait"></div>
  <div class="avatar" style="left:543px;top:155px;width:114px;height:114px;background:linear-gradient(180deg,#d4d4d6,#5a5e66)" role="img" aria-label="Portrait of Daniel Hart"></div>
  <div class="avatar" style="left:714px;top:172px;width:80px;height:80px;background:linear-gradient(180deg,#ececec,#c9bdb2)" role="img" aria-label="Client portrait"></div>
  <div class="name">DANIEL HART, CEO NORVEX</div>
  <div class="quote">
    <p>Rosalind is a decisive and fair leader who exemplifies strength, wisdom, and empathy. She always possesses a clear vision for the future and is willing to make bold decisions which are grounded in data, expertise, and intuition while remaining open to diverse perspectives.</p>
    <p>Rosalind's leadership style fosters an inclusive environment where every voice matters, empowering her team to excel and innovate. She was able to balance ambition with humanity and succeeded in prioritizing the well-being of her people, ensuring they feel valued and supported.</p>
    <p>In times of uncertainty her unwavering confidence and fairness inspire trust, driving the organization forward with resilience and integrity.</p>
  </div>
  <div class="dots"><span></span><span class="on"></span><span></span></div>
</section>

<section class="cta" role="img" aria-label="Blue-tinted photo of a professional at work">
  <h2 class="serif">Optimizing Travel with<br>Advanced Technology Consulting</h2>
  <a class="btn">Contact Me</a>
</section>

<section class="contact">
  <div class="eyebrow">GET IN TOUCH</div>
  <h2 class="serif">CONTACT <span class="accent">ME</span></h2>
  <div class="info" style="top:215px">
    <div class="ico"><svg width="18" height="22" viewBox="0 0 18 22"><path d="M9 1a7 7 0 0 0-7 7c0 5.3 7 13 7 13s7-7.7 7-13a7 7 0 0 0-7-7z" fill="#0677BA"/><circle cx="9" cy="8" r="2.6" fill="#fff"/></svg></div>
    <div><b>ADDRESS</b><span>123&nbsp; Ut wisi enim ad minim veniam,<br>quis nostrud exerci laoreet.</span></div>
  </div>
  <div class="info" style="top:299px">
    <div class="ico"><svg width="20" height="20" viewBox="0 0 24 24"><path d="M6.6 10.8a15 15 0 0 0 6.6 6.6l2.2-2.2a1 1 0 0 1 1-.25 11.4 11.4 0 0 0 3.6.57 1 1 0 0 1 1 1V20a1 1 0 0 1-1 1A17 17 0 0 1 3 4a1 1 0 0 1 1-1h3.5a1 1 0 0 1 1 1c0 1.25.2 2.45.57 3.57a1 1 0 0 1-.25 1z" fill="#0677BA"/></svg></div>
    <div><b>PHONE</b><span>(123) 456 789</span></div>
  </div>
  <div class="info" style="top:379px">
    <div class="ico"><svg width="20" height="16" viewBox="0 0 20 16"><rect x="1" y="1" width="18" height="14" rx="1.5" fill="#0677BA"/><path d="M1.5 2 10 9l8.5-7" fill="none" stroke="#fff" stroke-width="1.4"/></svg></div>
    <div><b>EMAIL</b><span>info@rosalindbranwell.com</span></div>
  </div>
  <form class="form">
    <div class="field" style="left:39px;top:45px;width:196px"><b>FIRST NAME</b><span>John</span></div>
    <div class="field" style="left:254px;top:45px;width:196px"><b>LAST NAME</b><span>Smith</span></div>
    <div class="field" style="left:39px;top:107px;width:196px"><b>EMAIL ADDRESS</b><span>Your email Address</span></div>
    <div class="field" style="left:254px;top:107px;width:196px"><b>PHONE NUMBER</b><span>Phone Number</span></div>
    <div class="field" style="left:39px;top:169px;width:411px;height:72px"><b>HOW CAN I HELP YOU</b><span>Leave Message</span></div>
    <a class="btn">Submit Now</a>
  </form>
  <svg class="dotgrid" width="160" height="170" viewBox="0 0 160 170">
    <g fill="#CADEEF">
      <circle cx="155" cy="4" r="2"/><circle cx="155" cy="20" r="2"/><circle cx="155" cy="36" r="2"/><circle cx="155" cy="52" r="2"/><circle cx="155" cy="68" r="2"/><circle cx="155" cy="84" r="2"/><circle cx="155" cy="100" r="2"/><circle cx="155" cy="116" r="2"/><circle cx="155" cy="132" r="2"/><circle cx="155" cy="148" r="2"/><circle cx="155" cy="164" r="2"/>
      <circle cx="3" cy="148" r="2"/><circle cx="20" cy="148" r="2"/><circle cx="37" cy="148" r="2"/><circle cx="54" cy="148" r="2"/><circle cx="71" cy="148" r="2"/><circle cx="88" cy="148" r="2"/><circle cx="105" cy="148" r="2"/><circle cx="122" cy="148" r="2"/><circle cx="139" cy="148" r="2"/>
      <circle cx="3" cy="164" r="2"/><circle cx="20" cy="164" r="2"/><circle cx="37" cy="164" r="2"/><circle cx="54" cy="164" r="2"/><circle cx="71" cy="164" r="2"/><circle cx="88" cy="164" r="2"/><circle cx="105" cy="164" r="2"/><circle cx="122" cy="164" r="2"/><circle cx="139" cy="164" r="2"/>
    </g>
  </svg>
</section>

<footer class="site-footer">
  <div class="brand">TBranwell</div>
  <div class="divider"></div>
  <nav class="foot-nav"><span>HOME</span><span>ABOUT ME</span><span>SERVICES</span></nav>
  <div class="copyright">© 2025 Rosalind Branwell. All Rights Reserved.</div>
  <div class="social"><span aria-label="Social link"></span><span aria-label="Social link"></span><span aria-label="Social link"></span></div>
</footer>

</body>
</html>
```